Combining web page

We need a PSD webpage design for our PrestaShop store that shows food combining rules, you can see an example that we put here, you can follow the same information and food image combinations. You are just doing the design but the images when implemented on the website will be clickable that goes to product categories, all text and images will be editable.

This is just an example:
http://merrowtonic.com/content/7-food-combining-rules

Target Market(s)

Natural Product and supplement industry

Industry/Entity Type

Store

Number of Pages Required

1 page

Colors

Designer to choose colors to be used in the design.

Requirements
Must have
• 1. Clear images.
• 2. Clear readable text.
• 3. Company name shown Merrow Tonic.
• 4. Follow the food rules as seen on the web page example, but not the same design.
• 5. Logo should be seen.
• 7. All text and images will be editable.
• 8. Make sure the food images are in their proper groups.
• 9. You are not coping the design we gave you but the details have to be the same, copy the text and the image food groups are important, you cannot just put any food in a group, and the combinations are important.
Nice to have
• Here is the website it is for http://merrowtonic.com/

```html
<!DOCTYPE html>
<html lang="en">
<head>
<meta charset="utf-8">
<title>Food Combining Rules – Merrow Tonic</title>
<link href="https://fonts.googleapis.com/css2?family=Roboto+Slab:wght@300;400;500;700&family=Lobster&display=swap" rel="stylesheet">
<style>
:root{
  --page:#e8e8e8;
  --board:#f5f2ec;
  --board-edge:#d9d2c4;
  --ink:#2f2f2f;
  --muted:#8d8d8d;
  --green:#6fae22;
  --leaf:#5f9e2a;
  --leaf-light:#9ccf4f;
  --amber:#fdb11a;
  --crimson:#a52422;
  --white:#ffffff;
  --line:#cfcfcf;
}
*{margin:0;padding:0;box-sizing:border-box}
html,body{width:1200px;height:853px;overflow:hidden}
body{background:var(--page);font-family:"Roboto Slab",serif;color:var(--ink);position:relative}

.vine{position:absolute;border-radius:40px;background:radial-gradient(circle at 40% 40%,var(--leaf-light),var(--leaf) 70%);opacity:.9}
.vine--left{left:58px;top:0;width:110px;height:250px}
.vine--right{left:1035px;top:0;width:112px;height:250px}

.header{position:absolute;left:98px;top:42px;width:1006px;height:200px;background:var(--board);border-bottom:6px solid var(--board-edge);box-shadow:0 8px 10px rgba(0,0,0,.12)}
.header__tagline{position:absolute;left:0;right:0;top:10px;text-align:center;font-size:12.5px;letter-spacing:.6px}
.header__login{position:absolute;left:867px;top:10px;font-size:13px}
.search{position:absolute;left:86px;top:53px;width:217px;height:25px;border-bottom:1px solid var(--ink);font-size:11px;font-style:italic;color:#555;padding:4px 4px}
.search svg{position:absolute;right:4px;top:2px}
.brand{position:absolute;left:0;right:0;top:58px;text-align:center;font-size:30px;font-weight:700;color:var(--green)}
.brand::before{content:"";display:inline-block;width:14px;height:14px;border-radius:50%;background:var(--green);margin-right:8px;vertical-align:middle}
.cart{position:absolute;left:829px;top:56px;font-size:16px;color:var(--green);display:flex;align-items:center;gap:9px}
.nav{position:absolute;left:0;right:0;top:140px;display:flex;justify-content:center;gap:37px;font-size:15px;letter-spacing:.6px}

.card{position:absolute;left:112px;top:300px;width:976px;height:560px;background:var(--white);overflow:hidden}
.card__title{position:absolute;left:0;right:0;top:26px;text-align:center;font-family:"Lobster",cursive;font-size:31px;font-weight:400;color:#444}
.card__title span{color:var(--green)}

.group{position:absolute;left:0;width:976px;height:110px;color:var(--white)}
.group--citrus{top:101px;background:var(--amber)}
.group--subacid{top:473px;background:var(--crimson)}
.group__num{position:absolute;left:0;top:0;width:83px;height:110px;font-size:82px;font-weight:500;text-align:center;line-height:120px}
.group__photo{position:absolute;left:83px;top:0;width:167px;height:110px}
.group__photo--citrus{background:radial-gradient(circle at 30% 40%,#f6a21d,#e57d12 60%,#e8d68c)}
.group__photo--berry{background:radial-gradient(circle at 40% 40%,#d2374a,#4b2234 60%,#2b3560)}
.group__name{position:absolute;left:271px;top:11px;font-size:15px;font-weight:700;padding-bottom:7px;border-bottom:1px solid rgba(255,255,255,.8);width:158px}
.group__list{position:absolute;left:271px;top:54px;font-size:15px;font-weight:300;line-height:20px;width:390px}
.group__brand{position:absolute;right:26px;top:38px;font-size:26px;font-weight:700}

.rules{position:absolute;top:237px;left:0;width:976px}
.rule{position:absolute;width:240px}
.rule__head{display:flex;align-items:center;gap:8px;font-size:15px;font-weight:500;color:#444}
.rule__items{list-style:none;margin-top:14px;font-size:11.5px;color:var(--muted);font-weight:500}
.rule__items li{margin-bottom:10px;line-height:14px}

.note{position:absolute;left:0;top:372px;width:976px;border-top:1px solid var(--line);padding:13px 17px}
.note__label{font-family:Arial,sans-serif;font-size:11.5px;font-weight:700;color:#222}
.note__text{margin-top:8px;font-size:11.5px;font-weight:300;color:var(--muted);line-height:16px}
</style>
</head>
<body>
<div class="vine vine--left" role="img" aria-label="Climbing ivy vine with green leaves"></div>
<div class="vine vine--right" role="img" aria-label="Climbing ivy vine with green leaves"></div>

<header class="header">
  <div class="header__tagline">TIMELESS FOODS FOR MODERN LIVING</div>
  <div class="header__login">Login ⌄</div>
  <div class="search">Search
    <svg width="20" height="20" viewBox="0 0 20 20"><circle cx="8" cy="8" r="6.5" fill="none" stroke="#333" stroke-width="1.4"/><line x1="13" y1="13" x2="19" y2="19" stroke="#333" stroke-width="1.6"/></svg>
  </div>
  <div class="brand">Merrow Tonic</div>
  <div class="cart">
    <svg width="24" height="22" viewBox="0 0 24 22"><path d="M2 9h20l-2 11H4z" fill="none" stroke="#444" stroke-width="1.5"/><path d="M6 9l6-7 6 7" fill="none" stroke="#444" stroke-width="1.5"/><line x1="9" y1="12" x2="9" y2="18" stroke="#444"/><line x1="12" y1="12" x2="12" y2="18" stroke="#444"/><line x1="15" y1="12" x2="15" y2="18" stroke="#444"/></svg>
    (0 Cart)
  </div>
  <nav class="nav"><span>OUR PRODUCTS</span><span>INGREDIENTS</span><span>HEALTH CONCERNS</span><span>OUR BLOGS</span><span>MORE</span></nav>
</header>

<main class="card">
  <h1 class="card__title">Food <span>Combining</span> Rules</h1>

  <section class="group group--citrus">
    <div class="group__num">1</div>
    <div class="group__photo group__photo--citrus" role="img" aria-label="Sliced oranges and lemons"></div>
    <h2 class="group__name">CITRUS-ACID FRUITS</h2>
    <p class="group__list">grapefruit, oranges, lemons, limes, tangelos, clementines, kumquat, and ugli fruit</p>
    <div class="group__brand">Merrow Tonic</div>
  </section>

  <div class="rules">
    <div class="rule" style="left:17px">
      <div class="rule__head"><svg width="17" height="17" viewBox="0 0 17 17"><path d="M2 8h3v8H2zM6 8l3-6c1.5 0 2 1 1.6 2.5L10 7h5l-1.5 9H6z" fill="none" stroke="#6fae22" stroke-width="1.4"/></svg>Combines Well</div>
      <ul class="rule__items"><li>Citrus-Acid Fruits</li><li>Fruits (sub-acid)</li><li>Neutral Fruits-Raw Nuts-Seeds</li></ul>
    </div>
    <div class="rule" style="left:267px">
      <div class="rule__head"><svg width="22" height="17" viewBox="0 0 22 17"><line x1="11" y1="1" x2="11" y2="15" stroke="#e0a020" stroke-width="1.4"/><line x1="3" y1="4" x2="19" y2="4" stroke="#e0a020" stroke-width="1.4"/><path d="M1 10l2-6 2 6zM17 10l2-6 2 6M6 16h10" fill="none" stroke="#e0a020" stroke-width="1.3"/></svg>Fair Compatibility</div>
      <ul class="rule__items"><li>Sweet Fruits-Palm Fruits</li><li>Melons</li></ul>
    </div>
    <div class="rule" style="left:517px">
      <div class="rule__head"><svg width="17" height="17" viewBox="0 0 17 17"><circle cx="8.5" cy="8.5" r="7" fill="none" stroke="#e0622a" stroke-width="1.8"/><line x1="4" y1="13" x2="13" y2="4" stroke="#e0622a" stroke-width="1.8"/></svg>Not Recommended</div>
      <ul class="rule__items"><li>Grains</li><li>Legumes-Sprouts</li></ul>
    </div>
    <div class="rule" style="left:767px">
      <div class="rule__head"><svg width="17" height="17" viewBox="0 0 17 17"><path d="M2 1h3v8H2zM6 9l3 6c1.5 0 2-1 1.6-2.5L10 10h5l-1.5-9H6z" fill="none" stroke="#c0262a" stroke-width="1.4"/></svg>Not Compatible</div>
      <ul class="rule__items"><li>Succulent Foods-Tomatoes</li><li>Vegetables (leafy, Flower, Root)</li></ul>
    </div>
  </div>

  <div class="note">
    <div class="note__label">Note:</div>
    <p class="note__text">Citrus fruits contain the highest levels of citric acid, as well as ascorbic acid and vitamin C. These fruits have a sharp flavor and can be tart. Citrus fruits include grapefruit, oranges, lemons, limes, tangelos, clementines, kumquat, and ugli fruit. Of all citrus fruits, lemons and limes contain the most citric acid, with about 4 grams of 100 grams of fruit.</p>
  </div>

  <section class="group group--subacid">
    <div class="group__num">2</div>
    <div class="group__photo group__photo--berry" role="img" aria-label="Mixed raspberries, blackberries and blueberries"></div>
    <h2 class="group__name">FRUITS (SUB-ACID)</h2>
    <p class="group__list">Apple, Papaya, Peach, Pear, Raspberry, Ugly Fruit, Apricot, Blackberry, Blueberry, Grape, Cherry, Mango, Mulberry</p>
    <div class="group__brand">Merrow Tonic</div>
  </section>
</main>
</body>
</html>
```